Product Description page for Hullwrap.com, References here just need a clean up redesign

Hi, were working on updating the product description page of our site hullwrap.com

Attached is a reference of what we drew on paint. We want to keep it pretty much the same as far as whats on there, the components with a few small adjustments and a clean actually designed look.

1. We want to remove the tabs (product description, warranty, reviews) and put it all in that main content area stretching down into sections. IE: Product Description section, followed by reviews, followed by warranty, below each other.
2. The side bar needs to be redesigned as far as the look and feel but the content and whats in there should stay the same.
3. The main banner area will be replaced shortly you do not have to worry about that.
4. Include a section or box for people to put in their email for a free Ebook.

Target Market(s)

people looking to easily view our boat cover products and buy without having to click too often or leave the page.

Industry/Entity Type

Online Shopping

Number of Pages Required

1 page

Requirements
Must have
• - Must update the sidebar
• - Must update the content area to remove the tabs and put the content from each tab sectioned off below each other (dummy text is fine for now for the tabs you cant view)
Nice to have
• - Cool place thats clean and functional to insert a section for people to put in their email to receive a free ebook
Should not have
• - too much change, we already know what we want and have a solid reference to work from.

```html
<!DOCTYPE html>
<html lang="en">
<head>
<meta charset="utf-8">
<title>Hullwrap.com – Product Detail</title>
<link href="https://fonts.googleapis.com/css2?family=Roboto+Condensed:wght@400;700&family=Roboto:wght@400;500;700&family=Source+Sans+3:wght@400;600&display=swap" rel="stylesheet">
<style>
:root{
  --ink:#222;
  --muted:#8a8a8a;
  --body:#9a9a9a;
  --brand:#1b8cc4;
  --royal:#2d4fd6;
  --navy:#1f3f9a;
  --line:#e2e2e2;
  --red:#e0262b;
  --price:#8a2a1a;
  --cover:#3645a8;
}
*{box-sizing:border-box;margin:0;padding:0}
html,body{width:1115px;height:1200px;overflow:hidden;background:#fff}
body{position:relative;font-family:"Source Sans 3",Arial,sans-serif;color:var(--ink)}

/* header */
.site-header{position:absolute;left:0;top:0;width:1062px;height:72px;background:linear-gradient(#fff,#f6f6f6 60%,#fff)}
.brand{position:absolute;left:216px;top:13px;display:flex;align-items:center;gap:6px;font:700 17px/1 "Roboto Condensed",sans-serif;color:#2b2b2b;letter-spacing:.2px}
.brand-mark{width:11px;height:11px;background:var(--brand)}
.phone{position:absolute;right:162px;top:9px;display:flex;align-items:center;gap:7px;font:700 18px/1 "Roboto Condensed",sans-serif;color:var(--royal)}
.hours{position:absolute;right:160px;top:28px;font:400 7.5px/1 Roboto,sans-serif;color:#777}
.main-nav{position:absolute;left:0;top:48px;width:1062px;height:24px;background:linear-gradient(#f7f7f7,#e6e6e6);border-top:1px solid #ddd}
.main-nav ul{list-style:none;display:flex;position:absolute;left:215px;top:6px}
.main-nav li{font:400 10px/12px Roboto,sans-serif;letter-spacing:1px;color:#555;padding:0 10px;border-left:1px solid #d0d0d0}
.main-nav li:first-child{padding-left:0;border-left:0}
.checkout{position:absolute;left:782px;top:47px;width:117px;height:21px;background:linear-gradient(#3f8fe0,#2268c4);border:1px solid #fff;box-shadow:0 0 0 1px #a9c8ec;color:#fff;font:700 7.5px/21px "Roboto Condensed",sans-serif;letter-spacing:.4px;display:flex;align-items:center;gap:7px;padding-left:9px}
.checkout span{font-weight:400}
.header-shadow{position:absolute;left:119px;top:72px;width:878px;height:2px;background:#e9e9e9}

/* breadcrumb */
.breadcrumb{position:absolute;left:216px;top:96px;font:400 7px/1 Roboto,sans-serif;color:#444}
.breadcrumb b{color:var(--navy);font-weight:500}

/* gallery */
.gallery-main{position:absolute;left:215px;top:127px;width:381px;height:237px;border:1px solid #d6d6d6;background:#fff;padding:10px 0 14px 2px}
.gallery-main div{width:100%;height:100%;background:linear-gradient(#fff 0,#fff 18%,#3a49ad 20%,#3645a8 40%,#e6e8ee 42%,#c9ccd6 60%,#f1f2f5 78%,#fff 100%)}
.thumbs{position:absolute;left:215px;top:384px;display:flex;align-items:center}
.thumb-arrow{width:16px;color:#aaa;font:400 11px/1 Roboto,sans-serif;text-align:center}
.thumb{width:39px;height:40px;border:1px solid #ccc;margin-right:3px}
.t1{background:linear-gradient(#eee,#b44 60%,#333)}
.t2{background:linear-gradient(135deg,#2f6fb8,#123d7a)}
.t3{background:linear-gradient(135deg,#ddd,#333)}
.t4{background:linear-gradient(#eee,#888)}
.t5{background:linear-gradient(#aaa,#111)}
.t6{background:linear-gradient(135deg,#555,#222 50%,#ccc)}

/* buy box sidebar */
.sidebar{position:absolute;left:0;top:0}
.product-title{position:absolute;left:613px;top:123px;white-space:nowrap;font:700 16.5px/1 "Roboto Condensed",sans-serif;color:var(--brand);text-transform:uppercase}
.product-price{position:absolute;left:613px;top:151px;white-space:nowrap;font:400 17px/1 "Source Sans 3",sans-serif;color:#333}
.buy-rule{position:absolute;left:613px;top:184px;width:286px;height:1px;background:var(--line)}
.facts{position:absolute;left:615px;top:198px;white-space:nowrap;font-size:8.8px;line-height:14px;color:#333;list-style:none}
.facts .regular{color:var(--red)}
.option-label{position:absolute;left:764px;white-space:nowrap;font-size:8.8px;color:#333}
.color-select{position:absolute;left:800px;top:196px;width:75px;height:22px;border:1px solid #ccc;border-radius:2px;padding:5px 0 0 5px}
.color-select i{display:block;width:54px;height:9px;background:var(--cover)}
.color-select svg{position:absolute;right:5px;top:8px}
.qty{position:absolute;left:800px;top:226px;width:43px;height:22px;border:1px solid #ccc;border-radius:2px;text-align:center;font:400 8px/20px Roboto,sans-serif}
.ship-badge{position:absolute;left:617px;top:271px}
.btn-cart{position:absolute;left:620px;top:318px;width:82px;height:24px;background:#111;color:#fff;white-space:nowrap;font:400 9px/24px "Source Sans 3",sans-serif;display:flex;align-items:center;gap:8px;padding-left:9px}
.btn-wish{position:absolute;left:711px;top:318px;width:94px;height:24px;border:1px solid var(--red);color:var(--red);white-space:nowrap;font:400 9px/22px "Source Sans 3",sans-serif;display:flex;align-items:center;gap:6px;padding-left:7px}

/* content sections */
.section-title{position:absolute;left:216px;font:400 12px/1 Roboto,sans-serif;color:var(--brand)}
.section-rule{position:absolute;left:215px;width:563px;height:1px;background:var(--line)}
.sub-title{position:absolute;left:216px;font:400 9.5px/1 Roboto,sans-serif;color:#222}
.copy{position:absolute;left:216px;width:560px;font-size:7.8px;line-height:14px;color:var(--body)}
.features{position:absolute;list-style:none;font-size:7.8px;line-height:14px;color:var(--body);white-space:nowrap}
.features li::before{content:"*";margin-right:6px}
.review-logo{position:absolute;left:214px;top:814px;width:48px;height:32px;border:1px solid #ddd;font:400 8px/30px "Source Sans 3",sans-serif;color:#222;text-align:center}
.quote-mark{position:absolute;left:273px;top:810px;font:700 26px/1 Georgia,serif;color:#ddd}

/* accessories */
.divider{position:absolute;left:119px;top:880px;width:877px;height:1px;background:var(--line)}
.addon{position:absolute;top:904px;height:53px;border:1px solid #ccc;display:flex;align-items:center;white-space:nowrap}
.addon-img{width:26px;height:32px;margin:0 8px 0 6px;flex:none}
.addon-name{font:500 7px/8px Roboto,sans-serif;color:var(--brand);text-transform:uppercase}
.addon-note{font:400 6.8px/1 Roboto,sans-serif;color:#888;margin-top:5px}
.addon-free{font:700 6.5px/1 Roboto,sans-serif;color:var(--red);margin-top:4px}
.addon-price{font:700 10.5px/1 Roboto,sans-serif;color:var(--price);margin-top:5px;display:flex;align-items:center;gap:6px}
.check{width:7px;height:7px;border:1px solid #999;background:#ddd;display:inline-block}

/* footer */
.footer-band{position:absolute;left:0;top:999px;width:1115px;height:7px;background:#eef0f3}
.footer-scene{position:absolute;left:0;top:1006px;width:1115px;height:106px;background:linear-gradient(#fbfcfd 0,#c9d3e2 20%,#7f92b5 45%,#5d7d4f 68%,#3c5a2c 80%,#7aa0cc 88%,#2a66b8 100%)}
.footer-sea{position:absolute;left:0;top:1112px;width:1115px;height:88px;background:linear-gradient(#2a62b6,#1d49a5 40%,#15339a)}
.email-signup{position:absolute;left:263px;top:1119px;width:590px;height:24px;border:1px solid #5f8ad8;background:linear-gradient(#2557c0,#1a43a8);display:flex;align-items:center;padding-left:14px}
.signup-label{font:700 8px/1 Roboto,sans-serif;color:#fff;white-space:nowrap}
.signup-input{margin-left:10px;width:113px;height:14px;background:#fff;border-radius:2px 0 0 2px}
.signup-btn{height:15px;width:52px;background:#f06410;color:#fff;font:500 7.5px/15px Roboto,sans-serif;padding-left:5px;border-radius:0 2px 2px 0;white-space:nowrap}
.signup-links{position:absolute;right:12px;top:8px;font:700 7.5px/1 Roboto,sans-serif;color:#fff;text-decoration:underline;display:flex;gap:6px;white-space:nowrap}
.footer-rule{position:absolute;left:263px;top:1155px;width:590px;height:1px;background:#4a72c9}
.legal{position:absolute;left:0;top:1166px;width:1115px;text-align:center;font:400 7px/8.5px Roboto,sans-serif;color:#7c92c8}
.legal a{color:#fff;text-decoration:underline}
</style>
</head>
<body>

<header class="site-header">
  <div class="brand"><span class="brand-mark"></span>Hullwrap.com</div>
  <div class="phone">
    <svg width="18" height="13" viewBox="0 0 18 13"><path d="M1 4c2-3 14-3 16 0l-1 2-3-1V3H5v2L2 6z" fill="#2d4fd6"/><rect x="4" y="6" width="10" height="6" rx="1" fill="#2d4fd6"/><circle cx="9" cy="9" r="1.6" fill="#fff"/></svg>
    (800) 555-0142
  </div>
  <div class="hours">Store Hours(M-F, 9:30AM - 6PM PST)</div>
</header>
<nav class="main-nav">
  <ul>
    <li>Boat Covers</li><li>Bass Boat Covers</li><li>T Top Boat Covers</li><li>Bimini Tops</li><li>Jet Ski Covers</li>
  </ul>
</nav>
<div class="checkout">
  <svg width="12" height="10" viewBox="0 0 12 10"><path d="M0 1h2l2 6h6l1-4H3" fill="none" stroke="#fff" stroke-width="1.3"/><circle cx="5" cy="9" r="1" fill="#fff"/><circle cx="9" cy="9" r="1" fill="#fff"/></svg>
  <div>CHECKOUT : <span>(0) Items</span> &#9662;</div>
</div>
<div class="header-shadow"></div>

<div class="breadcrumb">Home &gt; &nbsp;Boat Covers &gt; &nbsp;Center Console with Bow Rails &gt; &nbsp;<b>up to 16’8” Long and 90” Wide</b></div>

<div class="gallery-main"><div role="img" aria-label="Boat on a trailer wrapped in a blue fitted cover with black tie-down straps"></div></div>
<div class="thumbs">
  <span class="thumb-arrow">&#8249;</span>
  <div class="thumb t1" role="img" aria-label="Quality rating seal"></div>
  <div class="thumb t2" role="img" aria-label="Blue cover fabric detail"></div>
  <div class="thumb t3" role="img" aria-label="Strap buckle close-up"></div>
  <div class="thumb t4" role="img" aria-label="Cover hem detail"></div>
  <div class="thumb t5" role="img" aria-label="Tie-down strap detail"></div>
  <div class="thumb t6" role="img" aria-label="Bungee and hook set"></div>
  <span class="thumb-arrow">&#8250;</span>
</div>

<aside class="sidebar" aria-label="Purchase options">
  <h1 class="product-title">Lorem Ipsum is simply dummy text</h1>
  <div class="product-price">$331.50</div>
  <div class="buy-rule"></div>
  <ul class="facts">
    <li class="regular">Regular Price &nbsp;: &nbsp;$442</li>
    <li>You Save &nbsp;: &nbsp;$110.50</li>
    <li>Availableity &nbsp;: &nbsp;Ready to ship</li>
    <li>Ships &nbsp;: &nbsp;1 business day</li>
  </ul>
  <div class="option-label" style="top:202px">Color &nbsp;:</div>
  <div class="color-select"><i></i><svg width="7" height="5" viewBox="0 0 7 5"><path d="M1 1l2.5 2.5L6 1" fill="none" stroke="#555" stroke-width="1.2"/></svg></div>
  <div class="option-label" style="top:232px">Qty &nbsp;:</div>
  <div class="qty">1</div>

  <svg class="ship-badge" width="88" height="19" viewBox="0 0 88 19">
    <path d="M12 3h76l-5 6.5 5 6.5H12z" fill="#1f63d6"/>
    <circle cx="10" cy="9.5" r="9" fill="#f2b92b"/>
    <circle cx="10" cy="9.5" r="6" fill="#3a6fd0"/>
    <text x="25" y="12.5" font-family="Roboto,sans-serif" font-weight="700" font-size="7.5" fill="#fff">Free Shipping*</text>
  </svg>

  <div class="btn-cart">
    <svg width="12" height="10" viewBox="0 0 12 10"><path d="M0 1h2l2 6h6l1-4H3" fill="none" stroke="#fff" stroke-width="1.4"/><circle cx="5" cy="9" r="1" fill="#fff"/><circle cx="9" cy="9" r="1" fill="#fff"/></svg>
    Add to Cart
  </div>
  <div class="btn-wish">
    <svg width="10" height="9" viewBox="0 0 10 9"><path d="M5 9L1 5C-1 3 0 0 2.5 0 4 0 5 1.5 5 1.5S6 0 7.5 0C10 0 11 3 9 5z" fill="#e0262b"/></svg>
    Add to Wish List
  </div>
</aside>

<main>
  <h2 class="section-title" style="top:457px">Product Info</h2>
  <div class="section-rule" style="top:474px"></div>
  <h3 class="sub-title" style="top:489px">Description</h3>
  <p class="copy" style="top:507px">Lorem Ipsum is simply dummy text of the printing and typesetting industry. Lorem Ipsum has been the industry's standard dummy text ever since the 1500s, when an unknown printer took a galley of type and scrambled it to make a type specimen book. It has survived not only five centuries, but also the leap into electronic typesetting, remaining essentially unchanged..</p>
  <h3 class="sub-title" style="top:560px">Features</h3>
  <ul class="features" style="left:216px;top:581px">
    <li>Short sleeves</li><li>V-neck</li><li>Side slits</li><li>Cotton</li><li>Hand wash at 30 degrees</li>
  </ul>
  <ul class="features" style="left:379px;top:581px">
    <li>Do not bleach</li><li>Line dry in shade, inside out</li><li>Wash separately</li><li>Do not iron on print</li>
  </ul>

  <h2 class="section-title" style="top:671px;left:214px">Shipping &amp; Returns</h2>
  <div class="section-rule" style="top:688px;left:214px"></div>
  <h3 class="sub-title" style="top:697px;left:214px">FREE Shipping:</h3>
  <p class="copy" style="top:711px;left:214px">Shipping is FREE on Shopwave for ALL items with net price Rs.799/- or more. Some Sellers may offer FREE Shipping EVEN when the net price of the item is below Rs.799. Please check for applicable shipping charges in your checkout page. If Shipping charges are applicable, we charge Rs.49/- per order.</p>
  <p class="copy" style="top:743px;left:214px">In Metro cities our own fleet of Service Champions delivers your orders to your door. In other cities, our reputed courier partners like Swiftline, ParcelPoint, etc. ensure you receive your products at the earliest and in good condition.</p>

  <h2 class="section-title" style="top:788px;left:214px">Reviews</h2>
  <div class="section-rule" style="top:805px;left:214px"></div>
  <div class="review-logo">Corvale</div>
  <div class="quote-mark">&ldquo;</div>
  <p class="copy" style="top:818px;left:294px;width:490px">Go glamorous with this dress from Marlo that is bound to keep heads turning your way. Wear it with a pair of high heels and a cute hairband. tempor id aliquam metus. Phasellus feugiat rhoncus nulla quis dictum. Curabitur sed porta tortor, nec blandit risus.</p>
</main>

<div class="divider"></div>

<section aria-label="Accessories">
  <div class="addon" style="left:214px;width:133px">
    <div class="addon-img" style="background:linear-gradient(90deg,#fff 20%,#333 20%,#333 40%,#fff 40%)" role="img" aria-label="Support pole"></div>
    <div><div class="addon-name">Support Pole</div><div class="addon-note">Works for Boats and Trucks!</div><div class="addon-price">$30.75 <span class="check"></span></div></div>
  </div>
  <div class="addon" style="left:361px;width:156px">
    <div class="addon-img" style="background:linear-gradient(#2b4fb8 55%,#222 55%)" role="img" aria-label="Outboard motor cover"></div>
    <div><div class="addon-name">Boat Motor Cover</div><div class="addon-note">Heavy duty waterproof material!</div><div class="addon-price">$43.06 <span class="check"></span></div></div>
  </div>
  <div class="addon" style="left:532px;width:167px">
    <div class="addon-img" style="width:38px;background:radial-gradient(circle,#333 40%,#111 60%,#fff 62%)" role="img" aria-label="Strap and buckle pack"></div>
    <div><div class="addon-name">132 in. Straps and Buckl<br>Pack</div><div class="addon-free">FREE !</div><div class="addon-price">$26.14 <span class="check"></span></div></div>
  </div>
  <div class="addon" style="left:714px;width:133px">
    <div class="addon-img" style="width:34px;height:40px;background:radial-gradient(ellipse,#555,#1a1a1a 65%,#fff 67%)" role="img" aria-label="Black storage bag"></div>
    <div><div class="addon-name">Storage Bag</div><div class="addon-free">FREE !</div><div class="addon-price">$26.14 <span class="check"></span></div></div>
  </div>
</section>

<footer>
  <div class="footer-band"></div>
  <div class="footer-scene" role="img" aria-label="Marina full of sailboats in front of misty blue mountains"></div>
  <div class="footer-sea"></div>
  <form class="email-signup" aria-label="Email sign-up">
    <span class="signup-label">Sign Up To Win A FREE Boat Cover!</span>
    <span class="signup-input"></span>
    <span class="signup-btn">Subscribe &#9656;</span>
    <div class="signup-links"><span>Exchanges &amp; Returns</span><span>Contact Us</span></div>
  </form>
  <div class="footer-rule"></div>
  <div class="legal">Copyright © 2016 &nbsp;Hullwrap.com. All Rights Reserved<br>214 Harbor View Road, Port Calloway NY 10599<br><a>Privacy Policy</a></div>
</footer>

</body>
</html>
```